New Letterhead Design Project

i need a logo letterhead & compliment slips for my new company the name of the company is called Harwick Civil Engineers Ltd the work we do is foundations floor slabs drainage retaining walls block paving & tarmac

Industry/Entity Type

It Company

```html
<!DOCTYPE html>
<html lang="en">
<head>
<meta charset="utf-8">
<title>Harwick Civil Engineers Ltd — Letterhead</title>
<link rel="stylesheet" href="https://fonts.googleapis.com/css2?family=Jost:wght@400;500&display=swap">
<style>
  :root {
    --paper: #ffffff;
    --band-dark: #383838;
    --band-mid: #4b4b4b;
    --band-light: #5a5a5a;
    --ink-light: #f2f2f2;
    --mark-grey: #a9a9a9;
  }
  html, body {
    margin: 0;
    padding: 0;
    overflow: hidden;
    background: var(--paper);
  }
  .letterhead {
    position: relative;
    width: 900px;
    height: 1200px;
    overflow: hidden;
    background: var(--paper);
    font-family: "Jost", "Futura", sans-serif;
  }
  .letterhead__bands {
    position: absolute;
    inset: 0;
  }
  .brand {
    position: absolute;
    left: 22px;
    top: 36px;
    display: flex;
    align-items: center;
    gap: 8px;
  }
  .brand__square {
    width: 22px;
    height: 22px;
    background: var(--mark-grey);
  }
  .brand__name {
    color: var(--mark-grey);
    font-size: 15px;
    font-weight: 500;
    line-height: 1.1;
    letter-spacing: 0.5px;
    width: 100px;
  }
  .contact {
    position: absolute;
    left: 162px;
    top: 14px;
    margin: 0;
    padding: 0;
    list-style: none;
    color: var(--ink-light);
    font-size: 16.5px;
    font-weight: 400;
    line-height: 24px;
    letter-spacing: -0.2px;
  }
</style>
</head>
<body>
  <div class="letterhead">
    <svg class="letterhead__bands" width="900" height="1200" viewBox="0 0 900 1200" aria-hidden="true">
      <!-- header -->
      <path fill="var(--band-dark)" d="M0,0 H900 V62 Q420,90 0,255 Z"/>
      <path fill="var(--band-mid)" d="M0,185 Q330,100 750,0 H900 V62 Q420,90 0,255 Z"/>
      <path fill="var(--band-light)" d="M520,70 Q650,30 760,0 H900 V62 Q700,62 520,92 Z" opacity="0.6"/>
      <!-- footer -->
      <path fill="var(--band-mid)" d="M0,1200 V1148 Q520,1165 900,1085 V1200 Z"/>
      <path fill="var(--band-dark)" d="M0,1200 V1162 Q500,1178 900,1142 V1200 Z"/>
      <path fill="var(--band-dark)" d="M0,1200 V1175 Q300,1182 520,1200 Z"/>
    </svg>

    <div class="brand">
      <div class="brand__square"></div>
      <div class="brand__name">HARWICK CIVIL ENGINEERS LTD</div>
    </div>

    <ul class="contact">
      <li>Address 24 Larch Row, Elmsby, Thornfield TF4 8QD</li>
      <li>Email: harwickcivilltd@postmail.com</li>
      <li>Phone: 01632 960418</li>
      <li>Mob: 07700900362</li>
    </ul>
  </div>
</body>
</html>
```